Business Card Design

I would like to have business cards completely redesigned for my car ceramic coating and detailing business.
The cards uploaded are the current, the information needs to change but you can see our logo, I want something modern, professional and eye catching.

```html
<!DOCTYPE html>
<html lang="en">
<head>
<meta charset="utf-8">
<title>Prism Gloss – Business Card</title>
<link href="https://fonts.googleapis.com/css2?family=Montserrat:wght@400;500;600;800&display=swap" rel="stylesheet">
<style>
  :root {
    --page: #2b2b2d;
    --card: #1f2022;
    --ink: #f2f2f2;
    --ink-soft: #d9d9d9;
    --accent: #1d8ad8;
    --rule: #8a8a8a;
  }
  * { box-sizing: border-box; margin: 0; padding: 0; }
  html, body {
    width: 1200px; height: 900px; overflow: hidden;
    background: var(--page);
    font-family: "Montserrat", sans-serif;
  }
  .stage {
    width: 1200px; height: 900px;
    display: flex; flex-direction: column;
    align-items: center; justify-content: center; gap: 44px;
  }
  .card {
    position: relative;
    width: 640px; height: 366px;
    background: var(--card);
    border-radius: 12px;
    overflow: hidden;
    box-shadow: 0 10px 24px rgba(0,0,0,.35);
  }
  .card__band {
    position: absolute; left: 0; right: 0; bottom: 0;
    height: 16px; background: var(--accent);
  }
  .brand {
    font-weight: 800;
    color: var(--ink);
    letter-spacing: 2px;
    text-transform: uppercase;
    display: flex; align-items: center; justify-content: center; gap: 18px;
  }
  .brand__dot {
    width: 22px; height: 22px; border-radius: 50%;
    background: var(--accent);
  }
  .card--back .brand {
    position: absolute; left: 0; right: 0; top: 140px;
    font-size: 52px;
  }
  .card--front .brand {
    position: absolute; left: 0; right: 0; top: 38px;
    font-size: 44px;
  }
  .details {
    position: absolute; left: 58px; right: 40px; top: 138px;
    display: flex; align-items: stretch;
  }
  .person {
    width: 226px; text-align: right; padding-right: 24px;
    border-right: 1.5px solid var(--rule);
  }
  .person__name {
    color: var(--accent); font-weight: 600; font-size: 22px; letter-spacing: .5px;
    text-transform: uppercase; margin-bottom: 6px;
  }
  .person__role {
    color: var(--ink-soft); font-size: 15px; line-height: 1.45;
  }
  .contact {
    list-style: none; padding-left: 24px;
    display: flex; flex-direction: column; justify-content: center; gap: 7px;
  }
  .contact__item {
    display: flex; align-items: center; gap: 10px;
    color: var(--ink); font-size: 15.5px; font-weight: 500;
  }
  .contact__icon { width: 15px; height: 15px; flex: none; }
  .address {
    position: absolute; left: 146px; top: 282px;
    color: var(--ink); font-size: 16px; font-weight: 500;
  }
</style>
</head>
<body>
<main class="stage">
  <section class="card card--back" aria-label="Card back">
    <div class="brand"><span>Prism</span><span class="brand__dot"></span><span>Gloss</span></div>
    <div class="card__band"></div>
  </section>

  <section class="card card--front" aria-label="Card front">
    <div class="brand"><span>Prism</span><span class="brand__dot"></span><span>Gloss</span></div>

    <div class="details">
      <div class="person">
        <p class="person__name">Jordan Ellery</p>
        <p class="person__role">Owner I Operator<br>Automotive Detailing</p>
      </div>
      <ul class="contact">
        <li class="contact__item">
          <svg class="contact__icon" viewBox="0 0 24 24" fill="#1d8ad8"><path d="M6.6 10.8a15.1 15.1 0 0 0 6.6 6.6l2.2-2.2c.3-.3.7-.4 1-.2 1.1.4 2.3.6 3.6.6.6 0 1 .4 1 1V20c0 .6-.4 1-1 1A17 17 0 0 1 3 4c0-.6.4-1 1-1h3.5c.6 0 1 .4 1 1 0 1.3.2 2.5.6 3.6.1.3 0 .7-.2 1z"/></svg>
          0400 512 736
        </li>
        <li class="contact__item">
          <svg class="contact__icon" viewBox="0 0 24 24" fill="#1d8ad8"><path d="M2 5h20v14H2z" opacity=".0"/><path d="M3 5h18c.6 0 1 .4 1 1v.4l-10 6.2L2 6.4V6c0-.6.4-1 1-1zm-1 3.7 10 6.2 10-6.2V18c0 .6-.4 1-1 1H3c-.6 0-1-.4-1-1z"/></svg>
          bookings@prismgloss.com.au
        </li>
        <li class="contact__item">
          <svg class="contact__icon" viewBox="0 0 24 24" fill="none" stroke="#1d8ad8" stroke-width="2"><circle cx="12" cy="12" r="9.5"/><ellipse cx="12" cy="12" rx="4" ry="9.5"/><path d="M2.5 12h19"/></svg>
          www.prismgloss.com.au
        </li>
      </ul>
    </div>

    <p class="address">Unit 4/22 Harlow Court Belconnen ACT 2617</p>
    <div class="card__band"></div>
  </section>
</main>
</body>
</html>
```